Redesign our business card for more impact

We want to completely replace the back design of our card, and refresh or even change the front entirely. We are happy with our black Q7 logo and do not want to change it.
Our company address changed too. It is now 58 Corvallen, Larkmont, CA 92741
Updates

It was reported by Sketch Harbor email today that the uploaded files didnt upload. I am trying again.

Target Market(s)

Architects and Building Owners (People making multi-million dollar decisions)

Industry/Entity Type

Consulting Engineering

Contact Information for Business Card

Contact info on the front. "wallpaper" design on back with tag line on the back "Shaping What Comes Next"

Font styles to use
Sans Serif

Requirements
Must have
• A vivid, modern, impactful ...but tasteful back of card design. It should communicate our premier status, but grab attention as innovative. DESIGN SHOULD BE ELEGANT AND NOT TOO BUSY.
Nice to have
• Repeating pattern, multi-color, something creative...
Should not have
• Anything that looks too playful or that we are not serious professionals. It should also not be too boring or conservative.

```html
<!DOCTYPE html>
<html lang="en">
<head>
<meta charset="utf-8">
<title>Q7 Engineering — Business Card</title>
<link rel="stylesheet" href="https://fonts.googleapis.com/css2?family=Work+Sans:ital,wght@0,400;0,500;0,700;1,500&display=swap">
<style>
  :root {
    --backdrop: #d9d6d2;
    --card: #000000;
    --mark-grey: #4a4a4a;
    --deco-grey: #1c1c1c;
    --text-grey: #6f6f6f;
    --white: #ffffff;
  }
  * { margin: 0; padding: 0; box-sizing: border-box; }
  html, body { width: 1200px; height: 800px; overflow: hidden; }
  body {
    background: var(--backdrop);
    font-family: "Work Sans", Arial, sans-serif;
    position: relative;
  }
  .card {
    position: absolute;
    top: 245px;
    width: 540px;
    height: 309px;
    background: var(--card);
    overflow: hidden;
    box-shadow: 0 10px 24px rgba(0,0,0,0.25);
  }
  .card--front { left: 40px; }
  .card--rear { left: 620px; }

  /* Front */
  .brand-name {
    position: absolute;
    font-weight: 700;
    line-height: 1;
    letter-spacing: -0.02em;
  }
  .card--front .brand-name--small {
    left: 12px; top: 10px;
    font-size: 50px;
    color: var(--mark-grey);
  }
  .card--front .brand-name--deco {
    left: 165px; top: 22px;
    font-size: 240px;
    color: var(--deco-grey);
    letter-spacing: -0.04em;
  }
  .holder {
    position: absolute;
    left: 14px; top: 140px;
    color: var(--text-grey);
  }
  .holder__name {
    font-size: 11px;
    font-weight: 500;
    padding-bottom: 2px;
    border-bottom: 1px solid var(--text-grey);
    display: inline-block;
  }
  .holder__titles { font-size: 8.5px; line-height: 1.25; margin-top: 5px; }
  .contact, .address {
    position: absolute;
    bottom: 16px;
    font-size: 8.5px;
    line-height: 1.25;
    color: var(--text-grey);
  }
  .contact { left: 11px; }
  .address { right: 10px; text-align: left; }

  /* Rear */
  .wallpaper-name {
    position: absolute;
    font-size: 96px;
    font-weight: 700;
    line-height: 1;
    letter-spacing: -0.03em;
    color: var(--mark-grey);
  }
  .wallpaper-name--top { left: 150px; top: 12px; }
  .wallpaper-name--left { left: 14px; top: 100px; }
  .wallpaper-name--bottom { left: 100px; top: 190px; }
  .wallpaper-name--lead { left: 240px; top: 100px; color: var(--white); }
  .tagline {
    position: absolute;
    left: 318px; top: 204px;
    font-size: 11px;
    font-weight: 500;
    font-style: italic;
    color: var(--white);
    letter-spacing: 0.01em;
    white-space: nowrap;
  }
</style>
</head>
<body>
  <section class="card card--front" aria-label="Card front">
    <span class="brand-name brand-name--deco" aria-hidden="true">Q7</span>
    <span class="brand-name brand-name--small">Q7</span>
    <div class="holder">
      <p class="holder__name">DANIEL WHITCOMBE, PE</p>
      <p class="holder__titles">MSME, CEng<br>CEO/Principal</p>
    </div>
    <p class="contact">(415) 555-0147<br>daniel.whitcombe@q7eng.com<br>q7eng.com</p>
    <p class="address">58 Corvallen<br>Larkmont, CA 92741</p>
  </section>

  <section class="card card--rear" aria-label="Card rear">
    <span class="wallpaper-name wallpaper-name--top" aria-hidden="true">Q7</span>
    <span class="wallpaper-name wallpaper-name--left" aria-hidden="true">Q7</span>
    <span class="wallpaper-name wallpaper-name--bottom" aria-hidden="true">Q7</span>
    <span class="wallpaper-name wallpaper-name--lead">Q7</span>
    <p class="tagline">SHAPING WHAT COMES NEXT</p>
  </section>
</body>
</html>
```